Rancho Brisolo Wine Bottle Label

Hello! We are looking for a wine bottle label design for our private, family winery located in Chico, CA. The name of our home/ranch/vineyard is Rancho Brisolo ('the exit'), which is inspired by our hilltop location, panoramic views of the valley, and sensation of escaping from the busy world below.

We planted our vineyard in 2011 and are now bottling our first harvest from fall of 2013. We planted all Italian varietals on our land: syrah, primitivo, and montepulciano. The wine we make is the culmination of all the love, support and effort poured into the process by our family and friends.

The task at hand: we are looking for a clean, simple front and back wine label design.

Front Label Content:
RB and/or Rancho Brisolo
Estate Grown
Chico, CA
Varietal (use Syrah for placeholder)
Year (use 2013 for placeholder)

Back Label Content:
Running list of names of all family and friends who have participated in the process (use a text fill for placeholder)

Aesthetic Description:
Simple, clean, contemporary, text based design (see attached logo idea, Image #1)
Like the brown paper with stamped lettering look & feel
Like the classic clear label with gold lettering look & feel
Option to incorporated a simple background image/sketch of the view overlooking the valley (see attached Image #2 and #3)
Additional inspirational images attached for reference (Images #3- )

General Size Requirement:
Front Label - 4"tall by 3 1/2" wide
Back Label - 4"tall by 3 1/2" wide

Format:
Please submit Photoshop or Illustrator or InDesign Files and PDF/EPS Files.

Industry/Entity Type

Ranch

```html
<!DOCTYPE html>
<html lang="en">
<head>
<meta charset="utf-8">
<title>Rancho Brisolo – Syrah Labels</title>
<link href="https://fonts.googleapis.com/css2?family=Poiret+One&display=swap" rel="stylesheet">
<style>
  :root {
    --backdrop: #f1ede4;
    --kraft: #b8926b;
    --kraft-shade: #ad8760;
    --stamp-red: #7c1214;
    --ink-dark: #5a1a14;
  }
  * { margin: 0; padding: 0; box-sizing: border-box; }
  html, body {
    width: 1200px;
    height: 848px;
    overflow: hidden;
    background: var(--backdrop);
  }
  .canvas {
    position: relative;
    width: 1200px;
    height: 848px;
    font-family: "Poiret One", sans-serif;
    color: var(--stamp-red);
  }
  .label {
    position: absolute;
    top: 198px;
    width: 359px;
    height: 410px;
    background: linear-gradient(180deg, var(--kraft) 0%, var(--kraft-shade) 100%);
  }
  .label--front { left: 36px; }
  .label--back { left: 800px; }
  .label__frame {
    position: absolute;
    inset: 10px 12px 10px 12px;
    border: 3px solid var(--stamp-red);
  }
  .label__line {
    position: absolute;
    left: 0;
    right: 0;
    text-align: center;
    text-transform: uppercase;
    white-space: nowrap;
  }

  /* Front label */
  .front__name {
    top: 150px;
    font-size: 30px;
    line-height: 1;
  }
  .front__vintage { top: 262px; font-size: 32px; }
  .front__varietal { top: 312px; font-size: 32px; }
  .front__estate { top: 379px; font-size: 12px; color: var(--ink-dark); }

  /* Back label */
  .back__name {
    top: 50px;
    font-size: 20px;
    line-height: 1;
  }
  .back__thanks { top: 122px; font-size: 22px; }
  .back__people { top: 160px; font-size: 12px; }
  .back__info { top: 223px; font-size: 12px; line-height: 18px; }
  .back__legal { top: 308px; font-size: 12px; line-height: 18px; }
  .back__volume { top: 370px; font-size: 19px; }
  .back__abv {
    position: absolute;
    top: 370px;
    right: 30px;
    font-size: 19px;
  }
  .back__recycle {
    position: absolute;
    left: 32px;
    top: 368px;
    width: 26px;
    height: 24px;
  }
</style>
</head>
<body>
<main class="canvas">

  <section class="label label--front" aria-label="Front label">
    <div class="label__frame"></div>
    <p class="label__line front__name">Rancho Brisolo</p>
    <p class="label__line front__vintage">2013</p>
    <p class="label__line front__varietal">Syrah</p>
    <p class="label__line front__estate">Rancho Brisolo - Estate Grown</p>
  </section>

  <section class="label label--back" aria-label="Back label">
    <div class="label__frame"></div>
    <p class="label__line back__name">Rancho Brisolo</p>
    <p class="label__line back__thanks">With thanks to:</p>
    <p class="label__line back__people">Person A - Person B - Person C - Person D</p>
    <p class="label__line back__info">Wine info/ingredients: insert info of list<br>of ingredients &amp; taste notes in this section</p>
    <p class="label__line back__legal">Address - additional warnings to be placed<br>in this section</p>
    <svg class="back__recycle" viewBox="0 0 26 24" aria-label="Recycle symbol">
      <g fill="none" stroke="var(--ink-dark)" stroke-width="3" stroke-linejoin="round">
        <path d="M9 5 L13 2 L17 8"/>
        <path d="M20 12 L23 18 L16 20"/>
        <path d="M9 21 L3 21 L6 13"/>
      </g>
      <g fill="var(--ink-dark)">
        <path d="M15 9 L20 10 L19 5 Z"/>
        <path d="M14 17 L17 23 L18 17 Z"/>
        <path d="M4 12 L9 13 L6 9 Z"/>
      </g>
    </svg>
    <p class="label__line back__volume">750ml</p>
    <p class="back__abv">12%</p>
  </section>

</main>
</body>
</html>
```